"Eyebrow Threading Flyer Design"

We need a flyer design for a new service that will be provided in our established Beauty Salon in Toorak called "Threading". We provide all beauty services for our clients & would like to now introduce this very popular ancient method of hair removal.
Following are four "40% Off Threading Combo Packages" that will hopefully tempt new clients into our salon.
#Package 1- Eyebrow Threading plus Eyebrow Tint or Eyelash Tint Normally $53 Now $32
#Package 2- Eyebrow Threading plus Full Set Mink Lash Extensions
Normally $208 Now $125
#Package 3- Eyebrow Threading plus Glossa Manicure Or Pedicure
Normally $128 Now $77
#Package 4- Eyebrow Threading plus Collagen Facial
Normally $148 Now $89
We would like to see designs that use pink with whit or black to suit logo & business name & final design should be girly/feminine 7 fun.
On the back we would like the following details:
Velvet Dawn Beauty, "Lindell Court", shop 7, 418 Marlowe Street, 3187
Tel: 03 9471 2360, Email: info@velvetdawnbeauty.example, Web: www.velvetdawnbeauty.example
A map of exact location and business hours:
Mon 9am to 5pm, Tue 9am to 6pm, Wed 9am to 6pm, Thu 9am to 8pm, Fri 9am to 6pm, sat 9am to 5pm

Target Market(s)

Women between the ages of 20 to 60 years of age

Industry/Entity Type

Hair

Font styles to use
Script

Colors
e34297
000000

Requirements
Must have
• Pink and black or pink and white colors
Should not have
• Fake looking eyelashes displayed

```html
<!DOCTYPE html>
<html lang="en">
<head>
<meta charset="utf-8">
<title>Velvet Dawn Beauty – Threading Flyer</title>
<link rel="stylesheet" href="https://fonts.googleapis.com/css2?family=Tinos:wght@700&family=Arimo:wght@700&family=Archivo+Black&family=Cousine&display=swap">
<style>
:root{
  --crimson:#c11f4a;
  --brand-pink:#e5168c;
  --price-pink:#ef2d6c;
  --ink:#000;
  --paper:#fff;
  --header:#f4f4f4;
  --page:#fff;
  --label:#666;
}
*{box-sizing:border-box;margin:0;padding:0}
html,body{width:1063px;height:1200px;overflow:hidden;background:var(--page)}
.canvas{position:relative;width:1063px;height:1200px}
.side-label{position:absolute;top:88px;font:17px "Cousine",monospace;color:var(--label)}
.card{position:absolute;top:122px;width:456px;height:986px;overflow:hidden;background:var(--crimson);border:1px solid #222}
.card--front{left:47px}
.card--back{left:563px}

.header{position:absolute;left:0;top:0;width:456px;height:280px}
.header svg{position:absolute;inset:0}
.brand{position:absolute;left:0;right:0;top:190px;text-align:center;font-family:"Tinos",serif;font-weight:700;color:var(--brand-pink);line-height:1}
.brand__name{display:block;font-size:34px;letter-spacing:.5px}
.brand__sub{display:block;font-size:19px;letter-spacing:4px;margin-top:4px}
.brand__dot{position:absolute;left:50%;top:-92px;width:70px;height:70px;margin-left:-35px;border-radius:50%;background:#d9d9d9}

.offer-badge{position:absolute;left:15px;top:228px;width:166px;height:166px;border-radius:50%;background:var(--ink);color:var(--paper);font:700 25px/1.05 "Tinos",serif;display:flex;align-items:center;justify-content:center;text-align:center;z-index:3}

.package{position:absolute;left:-20px;width:500px}
.package__label{display:block;font:26px/1 "Archivo Black",sans-serif;color:var(--paper);letter-spacing:1px;text-shadow:2px 2px 0 #000,-1px -1px 0 #000,1px -1px 0 #000,-1px 1px 0 #000;margin-bottom:2px;white-space:nowrap}
.package__label--right{text-align:right;padding-right:44px}
.package__label--left{padding-left:46px}
.package__band{background:var(--ink);color:var(--paper);font:700 18.5px/27px "Arimo",sans-serif;padding:5px 20px 5px 46px;white-space:nowrap}
.price{color:var(--price-pink);font-size:27px;line-height:0;margin-left:4px}

.pkg-1{top:358px;transform:rotate(-7deg)}
.pkg-1 .package__label--right{padding-right:58px}
.pkg-2{top:474px;transform:rotate(-1deg)}
.pkg-3{top:582px;transform:rotate(-3deg)}
.pkg-4{top:677px;transform:rotate(-.5deg)}
.pkg-4 .package__band{padding:4px 20px 4px 46px}

.photo{position:absolute;left:0;width:456px}
.photo--front{top:768px;height:218px;background:linear-gradient(100deg,#e9d6cc 0%,#f1e2da 45%,#cfc9cd 100%)}
.photo--back{top:835px;height:151px;background:linear-gradient(90deg,#3a2b2a 0%,#d7b6a6 35%,#efe0d8 60%,#c5a294 100%)}

.map-frame{position:absolute;left:24px;top:285px;width:411px;height:289px;background:var(--ink);padding:16px 20px 18px 16px}
.map{width:100%;height:100%;background:linear-gradient(135deg,#e4e1da,#d6d3cc)}
.hours{position:absolute;left:24px;top:583px;width:425px;color:var(--paper);font:700 19px/20px "Arimo",sans-serif;letter-spacing:1.6px;white-space:pre}
.contact{position:absolute;left:21px;top:653px;width:411px;height:162px;background:var(--ink);color:var(--paper);text-align:center;font:21px/24px "Tinos",serif;padding-top:20px}
.contact__line{display:block}
.contact__link{display:block;color:var(--price-pink);font-weight:700}
</style>
</head>
<body>
<div class="canvas">
  <span class="side-label" style="left:47px">front</span>
  <span class="side-label" style="left:567px">back</span>

  <section class="card card--front">
    <div class="header">
      <svg width="456" height="280" viewBox="0 0 456 280" aria-hidden="true"><path d="M0 0H456V200Q228 310 0 200Z" fill="var(--header)"/></svg>
      <div class="brand"><span class="brand__dot"></span><span class="brand__name">VELVET DAWN</span><span class="brand__sub">BEAUTY</span></div>
    </div>
    <div class="offer-badge">40% OFF<br>Threading<br>Combo<br>Packages</div>

    <div class="package pkg-1">
      <span class="package__label package__label--right">PACKAGE 1</span>
      <div class="package__band">Eyebrow Threading plus Eyebrow Tint<br>or Eyelash Tint Normally $53 NOW <span class="price">$32</span></div>
    </div>
    <div class="package pkg-2">
      <span class="package__label package__label--right">PACKAGE 2</span>
      <div class="package__band">Eyebrow Threading plus Full Set Mink Lash<br>Extensions Normally $208 NOW <span class="price">$125</span></div>
    </div>
    <div class="package pkg-3">
      <span class="package__label package__label--left">PACKAGE 3</span>
      <div class="package__band">Eyebrow Threading plus Glossa Manicure<br>Or Pedicure Normally $128 NOW <span class="price">$77</span></div>
    </div>
    <div class="package pkg-4">
      <span class="package__label package__label--right">PACKAGE 4</span>
      <div class="package__band">Eyebrow Threading plus Collagen Facial<br>Normally $148 NOW <span class="price">$89</span></div>
    </div>

    <div class="photo photo--front" role="img" aria-label="Photo of a woman having her eyebrows shaped with thread"></div>
  </section>

  <section class="card card--back">
    <div class="header">
      <svg width="456" height="280" viewBox="0 0 456 280" aria-hidden="true"><path d="M0 0H456V200Q228 310 0 200Z" fill="var(--header)"/></svg>
      <div class="brand"><span class="brand__dot"></span><span class="brand__name">VELVET DAWN</span><span class="brand__sub">BEAUTY</span></div>
    </div>
    <div class="map-frame"><div class="map" role="img" aria-label="Street map showing the salon location"></div></div>
    <div class="hours">Mon  9AM to 5PM - Tue 9AM to 6PM
Wed  9AM to 6PM - Thu 9AM to 8PM
Fri     9AM to 6PM - Sat  9AM to 5PM</div>
    <div class="contact">
      <span class="contact__line">Velvet Dawn Beauty, "Lindell Court",</span>
      <span class="contact__line">shop 7, 418 Marlowe Street, 3187</span>
      <span class="contact__line">Tel: 03 9471 2360,</span>
      <span class="contact__link">Email: info@velvetdawnbeauty.example</span>
      <span class="contact__link">Web: www.velvetdawnbeauty.example</span>
    </div>
    <div class="photo photo--back" role="img" aria-label="Close-up photos of a woman's eye and a relaxed client during threading"></div>
  </section>
</div>
</body>
</html>
```